Flyer für Alltagsbegleitung
Zielgruppe
Firma: Tageshilfe am Fluss
Meine Zielgruppe sind alle Menschen, die im Alltag, Hilfe benötigen.
Aufgabenstellung
Der Flyer soll modern und und ansprechend aussehen. Es soll vermerkt sein, das ich als annerkannte Kraft, Entlastungsleistung nach

```html
<!DOCTYPE html>
<html lang="de">
<head>
<meta charset="utf-8">
<title>Tageshilfe am Fluss – Flyer</title>
<link rel="stylesheet" href="https://fonts.googleapis.com/css2?family=Barlow+Semi+Condensed:wght@600&family=Lexend:wght@500;600&family=Outfit:wght@600&display=swap">
<style>
  :root{
    --stage:#4a4a4a;
    --green:#69a936;
    --green-light:#b4d88c;
    --green-pale:#e6f1da;
    --ink:#1f4a2a;
    --white:#ffffff;
  }
  *{margin:0;padding:0;box-sizing:border-box}
  html,body{width:1200px;height:838px;overflow:hidden;background:var(--stage)}
  .page{position:absolute;top:33px;width:544px;height:772px;overflow:hidden}
  .page--front{left:38px;background:var(--white)}
  .page--back{left:627px;background:var(--green)}

  /* front */
  .front-top{position:absolute;left:0;top:0;width:544px;height:260px;
    background:linear-gradient(180deg,var(--green) 0%,#8cc257 55%,#e8efe2 100%)}
  .front-photo{position:absolute;left:0;top:215px;width:544px;height:390px;
    background:linear-gradient(180deg,#e3e6e3 0%,#d4d8d5 45%,#b79a7a 75%,#8e6a47 100%)}
  .front-title{position:absolute;left:40px;top:36px;font-family:"Barlow Semi Condensed",sans-serif;
    font-weight:600;font-size:70px;line-height:74px;color:var(--ink);letter-spacing:-0.5px}
  .front-wave{position:absolute;left:0;top:420px}
  .front-question{position:absolute;left:35px;top:528px;font-family:Outfit,sans-serif;font-weight:600;
    font-size:24px;line-height:29px;color:var(--white)}
  .front-info{position:absolute;left:0;top:595px;width:544px;height:177px;
    background:linear-gradient(180deg,var(--green-pale) 0%,var(--white) 55%)}
  .front-note{position:absolute;left:0;top:620px;width:544px;text-align:center;font-family:Lexend,sans-serif;
    font-weight:500;font-size:16.5px;line-height:21px;color:var(--ink)}
  .front-note .accent{color:var(--green)}
  .phone-pill{position:absolute;left:152px;top:708px;width:240px;height:32px;border-radius:16px;
    background:var(--green-light);display:flex;align-items:center;gap:16px;padding-left:5px;
    font-family:Lexend,sans-serif;font-weight:600;font-size:21px;letter-spacing:2px;color:var(--ink)}
  .phone-pill .dot{width:23px;height:23px;border-radius:50%;background:var(--green);display:flex;align-items:center;justify-content:center}

  /* back */
  .back-glow{position:absolute;left:0;top:0;width:544px;height:470px;
    background:linear-gradient(180deg,var(--green) 0%,#8cc35a 45%,#dbe9cf 90%)}
  .back-photo{position:absolute;left:0;top:440px;width:544px;height:200px;
    background:linear-gradient(90deg,#cfc9c2 0%,#e2cdb6 35%,#d8b394 60%,#e8e6e3 100%)}
  .services-pill{position:absolute;left:109px;top:30px;width:326px;height:39px;border-radius:20px;
    background:var(--green-light);text-align:center;font-family:Outfit,sans-serif;font-weight:600;
    font-size:23px;line-height:39px;color:var(--ink)}
  .service{position:absolute;width:180px;text-align:center;font-family:Lexend,sans-serif;font-weight:600;
    font-size:13.5px;line-height:14.5px;color:var(--ink)}
  .service .icon{display:block;width:53px;height:53px;margin:0 auto 9px;border-radius:50%;background:var(--white)}
  .section-title{position:absolute;left:0;top:322px;width:544px;display:flex;align-items:center;justify-content:center;gap:28px;
    font-family:Outfit,sans-serif;font-weight:600;font-size:28px;color:var(--ink)}
  .section-title::before,.section-title::after{content:"";width:54px;height:2px;background:var(--ink)}
  .intro{position:absolute;left:0;top:368px;width:544px;text-align:center;font-family:Outfit,sans-serif;
    font-weight:600;font-size:17.5px;line-height:22.5px;color:var(--ink)}
  .back-wave{position:absolute;left:0;top:560px}
  .help-pill{position:absolute;left:36px;top:646px;width:239px;height:33px;border-radius:17px;
    background:var(--green-light);padding-left:23px;font-family:Outfit,sans-serif;font-weight:600;
    font-size:18.5px;line-height:33px;color:var(--ink)}
  .contact{position:absolute;top:694px;font-family:Lexend,sans-serif;font-weight:500;font-size:17.5px;
    line-height:27px;letter-spacing:1.5px;color:var(--white)}
  .contact--name{left:60px}
  .contact--reach{left:190px}
  .contact-divider{position:absolute;left:162px;top:697px;width:2px;height:45px;background:var(--white)}
</style>
</head>
<body>

<section class="page page--front">
  <div class="front-top"></div>
  <div class="front-photo" role="img" aria-label="Foto: Betreuerin legt die Hände auf die Schultern eines lächelnden älteren Herrn mit Saftglas"></div>
  <h1 class="front-title">Tageshilfe<br>am Fluss</h1>
  <svg class="front-wave" width="544" height="180" viewBox="0 0 544 180" aria-hidden="true">
    <path d="M0 8 C120 0 220 40 330 100 C420 150 490 165 544 168 L544 180 L0 180 Z" fill="var(--green-light)"/>
    <path d="M0 22 C130 18 230 60 335 115 C420 158 490 170 544 174 L544 180 L0 180 Z" fill="var(--green)"/>
  </svg>
  <p class="front-question">Sie wünschen sich<br>Unterstützung im Alltag?</p>
  <div class="front-info"></div>
  <p class="front-note">Anerkannte Betreuungskraft gemäß <span class="accent">§ 45b SGB XI</span><br><span class="accent">Entlastungsleistungen</span> können direkt<br>mit der Pflegekasse abgerechnet werden.</p>
  <div class="phone-pill">
    <span class="dot"><svg width="13" height="13" viewBox="0 0 24 24"><path d="M6.6 10.8a15 15 0 0 0 6.6 6.6l2.2-2.2a1 1 0 0 1 1-.25 11.4 11.4 0 0 0 3.6.6 1 1 0 0 1 1 1V20a1 1 0 0 1-1 1A17 17 0 0 1 3 4a1 1 0 0 1 1-1h3.5a1 1 0 0 1 1 1c0 1.25.2 2.45.6 3.6a1 1 0 0 1-.25 1z" fill="#fff"/></svg></span>
    0157 4823 906
  </div>
</section>

<section class="page page--back">
  <div class="back-glow"></div>
  <div class="back-photo" role="img" aria-label="Foto: junge Hände halten die Hände eines älteren Menschen"></div>
  <h2 class="services-pill">Unsere Dienstleistungen</h2>

  <div class="service" style="left:27px;top:90px">
    <svg class="icon" viewBox="0 0 53 53"><circle cx="26.5" cy="26.5" r="26.5" fill="#fff"/><path d="M17 27 L26.5 18 L36 27 M20 25 V36 H33 V25" fill="none" stroke="var(--ink)" stroke-width="2.5"/></svg>
    Hilfe im Haushalt<br>&amp; beim Einkaufen</div>
  <div class="service" style="left:202px;top:90px">
    <svg class="icon" viewBox="0 0 53 53"><circle cx="26.5" cy="26.5" r="26.5" fill="#fff"/><path d="M26.5 36 L17 26 a5.5 5.5 0 0 1 9.5-6 a5.5 5.5 0 0 1 9.5 6 Z" fill="var(--ink)"/></svg>
    Arzt -<br>&amp; Freizeitbegleitung</div>
  <div class="service" style="left:360px;top:90px">
    <svg class="icon" viewBox="0 0 53 53"><circle cx="26.5" cy="26.5" r="26.5" fill="#fff"/><rect x="14" y="15" width="25" height="14" rx="3" fill="none" stroke="var(--ink)" stroke-width="2.5"/><circle cx="20" cy="36" r="3.5" fill="none" stroke="var(--ink)" stroke-width="2.2"/><circle cx="33" cy="36" r="3.5" fill="none" stroke="var(--ink)" stroke-width="2.2"/></svg>
    Gesellschaft<br>&amp; Gespräche</div>
  <div class="service" style="left:96px;top:207px">
    <svg class="icon" viewBox="0 0 53 53"><circle cx="26.5" cy="26.5" r="26.5" fill="#fff"/><path d="M13 24 H40 L37 36 H16 Z M19 24 L24 16 M34 24 L29 16" fill="none" stroke="var(--ink)" stroke-width="2.5"/></svg>
    Einkäufe<br>und Spaziergänge</div>
  <div class="service" style="left:285px;top:207px">
    <svg class="icon" viewBox="0 0 53 53"><circle cx="26.5" cy="26.5" r="26.5" fill="#fff"/><rect x="18" y="14" width="17" height="23" rx="2" fill="none" stroke="var(--ink)" stroke-width="2.5"/><path d="M22 21 H31 M22 26 H31 M22 31 H28" stroke="var(--ink)" stroke-width="2"/></svg>
    Hilfe bei Anträgen<br>&amp; Formularen</div>

  <h2 class="section-title">Betreuungsdienst</h2>
  <p class="intro">Als erfahrene und engagierte Betreuungskraft<br>unterstütze ich Sie persönlich dabei, Ihren Alltag<br>angenehmer und strukturierter zu gestalten.</p>

  <svg class="back-wave" width="544" height="212" viewBox="0 0 544 212" aria-hidden="true">
    <path d="M0 66 C180 40 380 20 544 0 L544 212 L0 212 Z" fill="var(--green-light)"/>
    <path d="M0 74 C180 50 380 28 544 10 L544 212 L0 212 Z" fill="var(--green)"/>
  </svg>
  <p class="help-pill">Brauchen Sie Hilfe?</p>
  <p class="contact contact--name">Mara<br>Velden</p>
  <span class="contact-divider"></span>
  <p class="contact contact--reach">0157 4823 906<br>maravelden@postfach.de</p>
</section>

</body>
</html>
```